Website Revamp: Favorzo.com

Just got a new logo looking for a web design to go with the business. I need the photoshop files and stock photos. No Word Press Please.

```html
<!DOCTYPE html>
<html lang="en">
<head>
<meta charset="utf-8">
<title>Favorzo — Cash for Cars</title>
<link href="https://fonts.googleapis.com/css2?family=Baloo+2:wght@600;700&family=Poppins:wght@300;400;500;600;700&display=swap" rel="stylesheet">
<style>
:root{
  --green:#58ad2f;
  --green-dark:#4a9826;
  --ink:#222;
  --muted:#777;
  --light:#999;
  --panel:#4c4748;
  --footer:#3b3b3b;
  --footer-text:#bdbdbd;
  --white:#fff;
  --orange:#f39c12;
}
*{margin:0;padding:0;box-sizing:border-box}
html,body{width:1200px;height:3500px;overflow:hidden}
body{font-family:'Poppins',sans-serif;color:var(--ink);background:var(--white);position:relative}
.abs{position:absolute}

/* header */
.site-header{position:absolute;left:0;top:0;width:1200px;height:102px;background:var(--white);border-bottom:1px solid #eee}
.brand{position:absolute;left:236px;top:40px;display:flex;align-items:center;gap:8px;font-weight:700;font-size:22px;color:var(--green)}
.brand-dot{width:18px;height:18px;border-radius:50%;background:var(--green)}
.nav a{position:absolute;top:52px;font-size:10.5px;font-weight:500;color:#555;text-decoration:none;letter-spacing:.5px}
.nav a.active{color:var(--green)}
.nav a.active::after{content:"";position:absolute;left:0;right:0;top:44px;height:2px;background:var(--green)}
.social-dot{position:absolute;top:47px;width:19px;height:19px;border-radius:50%;background:#a9a9a9}
.social-dot.first{background:var(--green)}
.menu-btn{position:absolute;left:951px;top:48px;width:15px;height:12px;border-top:2px solid #666;border-bottom:2px solid #666}
.menu-btn::after{content:"";position:absolute;left:0;right:0;top:3px;height:2px;background:#666}

/* hero */
.hero{position:absolute;left:0;top:102px;width:1200px;height:478px;background:linear-gradient(160deg,#3d4a2c 0%,#5a6340 25%,#8a2a2c 50%,#c7353b 62%,#4a4a4a 80%,#2f2f31 100%)}
.steps{position:absolute;left:236px;top:312px;width:730px;height:166px;background:rgba(255,255,255,.82)}
.step{position:absolute;top:0;width:220px;text-align:center}
.step-num{font-family:'Baloo 2',sans-serif;font-weight:700;font-size:34px;color:var(--green);line-height:1;margin-top:16px}
.step-icon{width:58px;height:50px;margin:8px auto 0;border-radius:8px;background:linear-gradient(135deg,#e74c3c,#3e8ed0 60%,#f1c40f)}
.step-text{font-size:15.5px;font-weight:500;color:#444;line-height:23px;margin-top:8px}

/* offer */
.offer{position:absolute;left:0;top:580px;width:1200px;height:435px;background:var(--panel)}
.offer-photo{position:absolute;left:0;top:0;width:600px;height:435px;background:linear-gradient(120deg,#d9d9dc 0%,#a9abb0 40%,#6e7076 70%,#b9bbbe 100%)}
.offer h2{position:absolute;left:660px;top:33px;width:300px;font-family:'Baloo 2',sans-serif;font-weight:700;font-size:25px;line-height:25px;color:var(--white)}
.offer .lead{position:absolute;left:660px;top:88px;width:270px;font-size:10px;line-height:15px;color:#ddd}
.feature{position:absolute;left:660px;display:flex;align-items:center;gap:14px;color:var(--white);font-size:12px;font-weight:500;letter-spacing:.6px;line-height:14px}
.feature svg{width:38px;height:38px;flex:none}
.btn{position:absolute;display:flex;align-items:center;justify-content:center;background:var(--green);color:var(--white);font-family:'Baloo 2',sans-serif;font-weight:700;font-size:17px;border-radius:30px;text-decoration:none}

/* listings */
.eyebrow{position:absolute;left:0;width:1200px;text-align:center;font-size:13.5px;color:#555;letter-spacing:.3px}
.section-title{position:absolute;left:0;width:1200px;text-align:center;font-size:18.5px;font-weight:700;letter-spacing:.8px}
.rule{position:absolute;width:44px;height:2px;background:var(--green)}
.intro{position:absolute;left:0;width:1200px;text-align:center;font-size:12.5px;line-height:16px;color:#555}
.card{position:absolute;width:225px;height:277px;background:var(--white);box-shadow:0 3px 12px rgba(0,0,0,.07)}
.card-photo{width:225px;height:164px}
.price{position:absolute;left:-6px;top:122px;width:56px;height:26px;background:var(--green);color:var(--white);font-size:12px;font-weight:600;display:flex;align-items:center;justify-content:center;letter-spacing:.6px}
.card-title{position:absolute;left:6px;top:178px;font-size:12.5px;font-weight:500;color:#333}
.card-loc{position:absolute;left:6px;top:200px;display:flex;align-items:center;gap:7px;font-size:9px;color:#888;letter-spacing:.6px}
.dots span{position:absolute;top:1765px;width:25px;height:3px;background:#aaa}
.dots span.on{background:var(--green)}

/* why */
.why{position:absolute;left:0;top:1867px;width:1200px;height:619px;background:linear-gradient(180deg,#50535a 0%,#3a3c41 35%,#1d1e21 70%,#2a2b2e 100%)}
.why .eyebrow{color:#eee}
.why .section-title{color:var(--white)}
.why-card{position:absolute;background:var(--white);text-align:center;padding:0 14px}
.why-card h3{font-size:11px;font-weight:600;letter-spacing:.5px;color:#222;white-space:nowrap}
.why-card p{font-size:8.4px;line-height:17px;color:#888;margin-top:14px}
.why-card.featured{background:var(--green)}
.why-card.featured h3,.why-card.featured p{color:var(--white)}
.why-card svg{display:block;margin:0 auto}

/* reviews */
.reviews-title{position:absolute;left:234px;top:2547px;font-size:20px;font-weight:500;color:#222}
.review{position:absolute;top:2642px;width:356px;height:162px;background:var(--white);box-shadow:0 3px 14px rgba(0,0,0,.08)}
.review h4{position:absolute;left:24px;top:54px;font-size:11.5px;font-weight:500;color:#333}
.review p{position:absolute;left:24px;top:79px;width:315px;font-size:9.6px;line-height:16px;color:#666}
.quote-mark{position:absolute;right:24px;top:14px;font-family:'Baloo 2',sans-serif;font-weight:700;font-size:54px;color:var(--green);line-height:1}
.stars{position:absolute;left:24px;top:122px;color:var(--orange);font-size:14px;letter-spacing:1px}

/* footer */
.site-footer{position:absolute;left:0;top:3025px;width:1200px;height:475px;background:var(--footer)}
.f-head{position:absolute;left:235px;font-size:9.5px;font-weight:500;color:var(--green);letter-spacing:.3px}
.f-col{position:absolute;font-size:8.4px;line-height:15.8px;color:var(--footer-text)}
.copyright{position:absolute;left:235px;top:3378px;font-size:8.4px;color:var(--footer-text)}
.f-social{position:absolute;top:3380px;width:11px;height:11px;border-radius:50%;background:#ddd}
</style>
</head>
<body>

<header class="site-header">
  <div class="brand"><span class="brand-dot"></span>Favorzo</div>
  <nav class="nav">
    <a class="active" href="#" style="left:419px">HOME</a>
    <a href="#" style="left:482px">ABOUT</a>
    <a href="#" style="left:568px">SERVICES</a>
    <a href="#" style="left:667px">CONTACT</a>
  </nav>
  <span class="social-dot first" style="left:801px" aria-label="Social profile"></span>
  <span class="social-dot" style="left:827px" aria-label="Social profile"></span>
  <span class="social-dot" style="left:854px" aria-label="Social profile"></span>
  <span class="social-dot" style="left:881px" aria-label="Social profile"></span>
  <span class="menu-btn"></span>
</header>

<section class="hero">
  <div role="img" aria-label="Red sports car driving on a road past green fields" style="position:absolute;inset:0"></div>
  <div class="steps">
    <div class="step" style="left:5px">
      <div class="step-num">1.</div>
      <div class="step-icon" role="img" aria-label="Truck with checklist illustration"></div>
      <div class="step-text">Tell Us About Your<br>Vehicle.</div>
    </div>
    <div class="step" style="left:260px">
      <div class="step-num">2.</div>
      <div class="step-icon" role="img" aria-label="Tow truck lifting a car illustration"></div>
      <div class="step-text">We Pick it up for<br>FREE!</div>
    </div>
    <div class="step" style="left:510px">
      <div class="step-num">3.</div>
      <div class="step-icon" role="img" aria-label="Hands exchanging cash illustration"></div>
      <div class="step-text" style="margin-top:16px">We Give You Cash!</div>
    </div>
    <svg class="abs" style="left:185px;top:52px" width="115" height="40" viewBox="0 0 115 40"><path d="M4 36 Q57 -8 111 36" fill="none" stroke="var(--green)" stroke-width="1.5" stroke-dasharray="3 3"/><path d="M4 36 l1-8 M4 36 l7-3 M111 36 l-1-8 M111 36 l-7-3" stroke="var(--green)" stroke-width="1.5"/></svg>
    <svg class="abs" style="left:440px;top:52px" width="115" height="40" viewBox="0 0 115 40"><path d="M4 36 Q57 -8 111 36" fill="none" stroke="var(--green)" stroke-width="1.5" stroke-dasharray="3 3"/><path d="M4 36 l1-8 M4 36 l7-3 M111 36 l-1-8 M111 36 l-7-3" stroke="var(--green)" stroke-width="1.5"/></svg>
  </div>
</section>

<section class="offer">
  <div class="offer-photo" role="img" aria-label="Two businessmen shaking hands across a desk"></div>
  <h2>Fill Out Our Form for an Instant Offer</h2>
  <p class="lead">We don't sell your information, we will only contact you about your car.</p>
  <div class="feature" style="top:154px">
    <svg viewBox="0 0 38 38"><path d="M6 17h7v16H6z M13 18l6-10c2-2 5-1 4 3l-2 6h9c2 0 3 2 2 4l-3 10c-1 2-2 2-4 2H13" fill="none" stroke="var(--green)" stroke-width="2" stroke-linejoin="round"/></svg>
    TRUSTED BUYER</div>
  <div class="feature" style="top:208px">
    <svg viewBox="0 0 38 38"><circle cx="19" cy="8" r="4" fill="none" stroke="var(--green)" stroke-width="1.8"/><path d="M3 20l8-3 8 5 8-5 8 3M5 22v11M33 22v11M11 25l6 5M21 30l6-5" fill="none" stroke="var(--green)" stroke-width="1.8" stroke-linecap="round"/></svg>
    THOUSANDS OF HAPPY<br>SELLERS</div>
  <div class="feature" style="top:262px">
    <svg viewBox="0 0 38 38"><path d="M4 20 L20 4 L34 4 L34 18 L18 34 Z" fill="none" stroke="var(--green)" stroke-width="2" stroke-linejoin="round"/><circle cx="27" cy="11" r="2.5" fill="var(--green)"/><path d="M16 15v10M19 17c-1-1-5-1-5 1s5 1 5 3-4 2-5 1" fill="none" stroke="var(--green)" stroke-width="1.6"/></svg>
    GET AN OFFER<br>INSTANTLY ONLINE!</div>
  <a class="btn" href="#" style="left:662px;top:341px;width:227px;height:44px">Get an Offer</a>
</section>

<p class="eyebrow" style="top:1077px">WITH FAVORZO</p>
<h2 class="section-title" style="top:1097px">CASH OFFERS MADE DAILY!</h2>
<span class="rule" style="left:578px;top:1126px"></span>
<p class="intro" style="top:1149px">Receive cash on the spot for your vehicle!<br>It doesn't matter how bad of shape it is in, we'll take it!</p>

<article class="card" style="left:236px;top:1222px">
  <div class="card-photo" role="img" aria-label="White sedan parked outdoors" style="background:linear-gradient(160deg,#dfe3e6,#f5f5f5 50%,#8c8f8a)"></div>
  <span class="price">$360</span>
  <h3 class="card-title">2014 Arden Solace</h3>
  <p class="card-loc"><svg width="9" height="12" viewBox="0 0 9 12"><path d="M4.5 0C2 0 0 2 0 4.5 0 7.5 4.5 12 4.5 12S9 7.5 9 4.5C9 2 7 0 4.5 0z" fill="var(--green)"/><circle cx="4.5" cy="4.5" r="1.7" fill="#fff"/></svg>Washington, USA</p>
</article>
<article class="card" style="left:488px;top:1222px">
  <div class="card-photo" role="img" aria-label="Red coupe parked on a lawn" style="background:linear-gradient(160deg,#9fb3c6,#c9302c 55%,#6f7c4e)"></div>
  <span class="price">$295</span>
  <h3 class="card-title">2003 Kestrel Meridian</h3>
  <p class="card-loc"><svg width="9" height="12" viewBox="0 0 9 12"><path d="M4.5 0C2 0 0 2 0 4.5 0 7.5 4.5 12 4.5 12S9 7.5 9 4.5C9 2 7 0 4.5 0z" fill="var(--green)"/><circle cx="4.5" cy="4.5" r="1.7" fill="#fff"/></svg>Washington, DC</p>
</article>
<article class="card" style="left:742px;top:1222px">
  <div class="card-photo" role="img" aria-label="Grey sedan in a parking lot" style="background:linear-gradient(160deg,#8aa0b8,#6b6f75 55%,#9a9a96)"></div>
  <span class="price">$265</span>
  <h3 class="card-title">2010 Brant Vireo</h3>
  <p class="card-loc"><svg width="9" height="12" viewBox="0 0 9 12"><path d="M4.5 0C2 0 0 2 0 4.5 0 7.5 4.5 12 4.5 12S9 7.5 9 4.5C9 2 7 0 4.5 0z" fill="var(--green)"/><circle cx="4.5" cy="4.5" r="1.7" fill="#fff"/></svg>Ft. Lauderdale, FL</p>
</article>
<article class="card" style="left:236px;top:1490px">
  <div class="card-photo" role="img" aria-label="Dark grey sedan parked by trees" style="background:linear-gradient(160deg,#4f7a3a,#5b5e63 55%,#8b8c8a)"></div>
  <span class="price">$360</span>
  <h3 class="card-title">2016 Velden Juno</h3>
  <p class="card-loc"><svg width="9" height="12" viewBox="0 0 9 12"><path d="M4.5 0C2 0 0 2 0 4.5 0 7.5 4.5 12 4.5 12S9 7.5 9 4.5C9 2 7 0 4.5 0z" fill="var(--green)"/><circle cx="4.5" cy="4.5" r="1.7" fill="#fff"/></svg>Dallas, TX</p>
</article>
<article class="card" style="left:488px;top:1490px">
  <div class="card-photo" role="img" aria-label="Black sedan in front of a garage door" style="background:linear-gradient(160deg,#9ea3a8,#2a2c30 55%,#6b6d70)"></div>
  <span class="price">$295</span>
  <h3 class="card-title">2011 Halvar Corsa</h3>
  <p class="card-loc"><svg width="9" height="12" viewBox="0 0 9 12"><path d="M4.5 0C2 0 0 2 0 4.5 0 7.5 4.5 12 4.5 12S9 7.5 9 4.5C9 2 7 0 4.5 0z" fill="var(--green)"/><circle cx="4.5" cy="4.5" r="1.7" fill="#fff"/></svg>Providence, RI</p>
</article>
<article class="card" style="left:742px;top:1490px">
  <div class="card-photo" role="img" aria-label="Beige sedan parked on grass" style="background:linear-gradient(160deg,#7a7f6a,#c9bda8 55%,#8d8a7c)"></div>
  <span class="price">$265</span>
  <h3 class="card-title">2008 Corvane Lido</h3>
  <p class="card-loc"><svg width="9" height="12" viewBox="0 0 9 12"><path d="M4.5 0C2 0 0 2 0 4.5 0 7.5 4.5 12 4.5 12S9 7.5 9 4.5C9 2 7 0 4.5 0z" fill="var(--green)"/><circle cx="4.5" cy="4.5" r="1.7" fill="#fff"/></svg>Bothel, WA</p>
</article>
<div class="dots"><span class="on" style="left:550px"></span><span style="left:587px"></span><span style="left:624px"></span></div>

<section class="why">
  <div role="img" aria-label="Black luxury sedan parked at dusk beside a building" style="position:absolute;inset:0"></div>
  <p class="eyebrow" style="top:56px">WHY US</p>
  <h2 class="section-title" style="top:76px">THE FAVORZO DIFFERENCE</h2>
  <span class="rule" style="left:578px;top:105px"></span>

  <div class="why-card" style="left:236px;top:177px;width:229px;height:228px">
    <svg style="margin-top:26px" width="62" height="56" viewBox="0 0 62 56"><rect x="4" y="10" width="38" height="22" fill="none" stroke="var(--green)" stroke-width="1.8"/><rect x="8" y="4" width="38" height="22" fill="none" stroke="var(--green)" stroke-width="1.8" transform="rotate(-8 27 15)"/><circle cx="23" cy="21" r="5" fill="none" stroke="var(--green)" stroke-width="1.8"/><g fill="#fff" stroke="var(--green)" stroke-width="1.8"><ellipse cx="50" cy="30" rx="9" ry="3"/><path d="M41 30v16c0 2 4 3 9 3s9-1 9-3V30"/><path d="M41 35c0 2 4 3 9 3s9-1 9-3M41 40c0 2 4 3 9 3s9-1 9-3" fill="none"/></g></svg>
    <h3 style="margin-top:20px">CASH ON THE SPOT!</h3>
    <p>Offering check, app payments, or bank instant transfers for your car! Of course, we also offer a standard check as well. Our professional drivers will hand deliver your check.</p>
  </div>

  <div class="why-card featured" style="left:485px;top:159px;width:231px;height:268px">
    <svg style="margin-top:50px" width="44" height="58" viewBox="0 0 44 58"><path d="M8 2h26l8 8v46H8z" fill="none" stroke="#fff" stroke-width="2"/><path d="M2 8h4M2 8v48h34" fill="none" stroke="#fff" stroke-width="2"/><path d="M15 18h20M15 25h20M15 32h20M15 39h20M15 46h14" stroke="#fff" stroke-width="2"/></svg>
    <h3 style="margin-top:24px">PROFESSIONAL TITLE HANDLERS</h3>
    <p>Have an issue with the title? No Problem. Our certified, professional drivers are well trained and can help you transfer that title in no time. We've been doing this quite a while.</p>
  </div>

  <div class="why-card" style="left:735px;top:177px;width:230px;height:229px">
    <svg style="margin-top:38px" width="62" height="46" viewBox="0 0 62 46"><path d="M12 6h38l6 14H6z" fill="none" stroke="var(--green)" stroke-width="2" stroke-linejoin="round"/><rect x="3" y="20" width="56" height="16" rx="3" fill="none" stroke="var(--green)" stroke-width="2"/><circle cx="13" cy="28" r="3" fill="none" stroke="var(--green)" stroke-width="2"/><circle cx="49" cy="28" r="3" fill="none" stroke="var(--green)" stroke-width="2"/><path d="M24 28h14M8 36v7h8v-7M46 36v7h8v-7" fill="none" stroke="var(--green)" stroke-width="2"/></svg>
    <h3 style="margin-top:22px">WE BUY ALL CAR TYPES</h3>
    <p>Every scrap car has value, even if you might not think so. We're happy to take them off your hands and recycle them. Saving our planet is a priority and one less car wasting</p>
  </div>

  <a class="btn" href="#" style="left:461px;top:498px;width:278px;height:50px">Hire a Professional</a>
</section>

<h2 class="reviews-title">Committed to Excellence</h2>
<span class="rule" style="left:234px;top:2578px;width:54px"></span>
<svg class="abs" style="left:927px;top:2561px" width="42" height="16" viewBox="0 0 42 16"><path d="M10 2 L4 8 L10 14 M32 2 L38 8 L32 14" fill="none" stroke="#888" stroke-width="1.5"/></svg>

<article class="review" style="left:235px">
  <span class="quote-mark">”</span>
  <h4>Fast and Simple</h4>
  <p>Called in the morning. They came, wrote me a check, and took my car before I finished my lunch.</p>
  <span class="stars">★★★★★</span>
</article>
<article class="review" style="left:610px">
  <span class="quote-mark">”</span>
  <h4>It was much better than I anticipated.</h4>
  <p>The pickup driver was professional, well-dressed, and explained everything. He wrote me a check right then and there.</p>
  <span class="stars">★★★★★</span>
</article>

<a class="btn" href="#" style="left:461px;top:2892px;width:278px;height:50px">Try it Out - Cash On the Spot!</a>

<footer class="site-footer"></footer>
<p class="f-head" style="top:3082px">POPULAR SEARCHES</p>
<p class="f-col" style="left:235px;top:3101px">We buy cars<br>Cash for cars<br>Scrap my car<br>Cash for Junk Cars</p>
<p class="f-col" style="left:383px;top:3101px">Sell Junk Car<br>Best way to sell a car<br>Used Car Buyer<br>Where can I sell my car</p>
<p class="f-col" style="left:554px;top:3101px">Cash for clunkers<br>We buy cars<br>Cash for cars<br>Scrap my car</p>
<p class="f-col" style="left:704px;top:3101px">Cash for Junk Cars<br>Sell Junk Car<br>Best way to sell a car<br>Junk car buyer</p>
<p class="f-col" style="left:857px;top:3101px">Junk car buyer<br>Used Car Buyer<br>Where can I sell my car<br>Cash for clunkers</p>

<p class="f-head" style="top:3180px">POPULAR CITIES</p>
<p class="f-col" style="left:235px;top:3199px">Washington DC<br>Sterling, VA<br>New York<br>Los Angeles<br>Seattle</p>
<p class="f-col" style="left:383px;top:3199px">Miami<br>Ft. Lauderdale<br>West Palm Beach<br>DC Metro Area<br>Dallas, TX</p>
<p class="f-col" style="left:554px;top:3199px">Washington DC<br>Sterling, VA<br>New York<br>Los Angeles<br>Seattle</p>
<p class="f-col" style="left:704px;top:3199px">Miami<br>Ft. Lauderdale<br>West Palm Beach<br>DC Metro Area<br>Dallas, TX</p>
<p class="f-col" style="left:857px;top:3199px">Miami<br>Ft. Lauderdale<br>West Palm Beach<br>DC Metro Area<br>Dallas, TX</p>

<p class="f-head" style="top:3291px">POPULAR VEHICLES</p>
<p class="f-col" style="left:235px;top:3311px">Rydell Nova<br>Nakari Sentio</p>
<p class="f-col" style="left:383px;top:3311px">Pellar Grand Tour<br>Arden Petal</p>
<p class="f-col" style="left:554px;top:3311px">Rydell Caravel<br>Arden Solace</p>
<p class="f-col" style="left:704px;top:3311px">Corvane Ranger<br>Nakari Apex</p>
<p class="f-col" style="left:857px;top:3311px">Brant Voyager<br>Brant Fokal</p>

<p class="copyright">© Favorzo, LLC 2020 - All Rights Reserved</p>
<span class="f-social" style="left:857px" aria-label="Social profile"></span>
<span class="f-social" style="left:889px" aria-label="Social profile"></span>
<span class="f-social" style="left:920px" aria-label="Social profile"></span>
<span class="f-social" style="left:953px" aria-label="Social profile"></span>

</body>
</html>
```